南谷 睦月というペンネームで活動しているものです。

本業は組織・人財開発領域に特化した支援を行う会社において、
企画の提案、プロジェクトマネジメント、依頼後の進捗管理など、
お客様の中に自身も入りながら、経営を変えていくような支援を行っています。

ご依頼をさせていただく表紙デザインですが、
9月16日にPagoraにて、下記の内容を発行いたしました。
============================
現場を変える人が大切にする4つの視点:
~挑戦した人々の物語から静かに学び取る~

www.bookvale-store.jp/item/Q72KD4MX3N
こちらの内容について、発行に向けた表紙手配が間に合わなかったこともあり、
一旦はデザインを自身で考え、発行をいたしましたが、
表紙は書籍の顔ということもあり、作成依頼を進めることに決めました。

デザイン制作にあたって検討いただきたいのは下記2点です。

検討に当たってのポイントは下記2点です。
① 悩みに対しての答えが見つかるような印象を持てる
② あまり複雑すぎないデザインであること

① 悩みに対しての答えが見つかるような印象を持てる
・取り上げたPagoraでは、スキル・ノウハウ本ではなく、
実践されている方が直面されたエピソードをもとにして、
悩みを解決するためのヒントを取り上げています。
そのようなニュアンスが感じられるようなデザインに期待です。

② あまり複雑なデザインではないこと
・凝ったデザインよりは、わかりやすいデザインを好む方です。
複雑なカラーよりは、色を限りながらも、与えられた題材に対しての
表現を頂けるようなデザインが好みではあります。
※ が、良いものが出てくれば、それ限りではございませんので、
あくまで、現時点の好みとしてお伝えを致します

最終的に今回のコンペでは「R_hoshidaさん」のデザインを採用させて頂きます。
重視した点は改めて、下記の2点がベースとなります。
① 悩みに対しての答えが見つかるような印象を持てる
② あまり複雑なデザインではないこと
絵で①のイメージを喚起しつつ、今回の書籍で押し出していることを文字で強調いただく構成となっており、②の点からも適切と考えて採択をさせて頂きました。

改めて、この度はご提案をいただきましてありがとうございます。

引き続き、個人的な目標としては3か月~6か月に1回の頻度で、
Pagora向けの発行物を執筆していく予定です。
また、このような形でご支援の相談をさせていただきますので、
よろしければ是非、お力添えをどうぞお願い申し上げます。

```html
<!DOCTYPE html>
<html lang="ja">
<head>
<meta charset="utf-8">
<title>現場を変える人が大切にする4つの視点</title>
<link rel="stylesheet" href="https://fonts.googleapis.com/css2?family=Noto+Sans+JP:wght@500;700;900&family=Noto+Serif+JP:wght@600;700&display=swap">
<style>
  :root {
    --cover-red: #b3121c;
    --accent-yellow: #ffe600;
    --paper: #ffffff;
    --ink: #222222;
    --wood-light: #efe6da;
    --wood-mid: #d9c3a5;
    --wood-dark: #b48e64;
  }
  html, body {
    margin: 0;
    padding: 0;
    overflow: hidden;
    background: var(--paper);
  }
  .cover {
    position: relative;
    width: 749px;
    height: 1200px;
    overflow: hidden;
    background: var(--paper);
    font-family: "Noto Sans JP", sans-serif;
  }
  .title-panel {
    position: absolute;
    left: 0;
    top: 0;
    width: 749px;
    height: 785px;
    background: var(--cover-red);
    color: var(--paper);
    text-align: center;
  }
  .title-line {
    position: absolute;
    left: 0;
    width: 100%;
    margin: 0;
    font-weight: 700;
    font-size: 150px;
    line-height: 1;
    letter-spacing: 6px;
  }
  .title-line.first { top: 92px; }
  .title-line.second { top: 272px; }
  .title-line .highlight { color: var(--accent-yellow); }
  .title-lead {
    position: absolute;
    top: 490px;
    left: 0;
    width: 100%;
    font-weight: 700;
    font-size: 36px;
    letter-spacing: 2px;
  }
  .title-lead .gap { display: inline-block; width: 16px; }
  .title-main {
    position: absolute;
    top: 575px;
    left: 0;
    width: 100%;
    font-weight: 700;
    font-size: 62px;
    letter-spacing: 28px;
    padding-left: 28px;
    box-sizing: border-box;
  }
  .author {
    position: absolute;
    top: 705px;
    left: 0;
    width: 100%;
    font-family: "Noto Serif JP", serif;
    font-weight: 700;
    font-size: 32px;
    letter-spacing: 4px;
  }
  .growth-scene {
    position: absolute;
    right: 0;
    top: 785px;
    width: 420px;
    height: 415px;
    background: linear-gradient(180deg, var(--wood-light) 0%, var(--paper) 35%, var(--wood-mid) 78%, var(--wood-dark) 100%);
  }
  .tagline {
    position: absolute;
    top: 806px;
    left: 38px;
    margin: 0;
    font-weight: 500;
    font-size: 29px;
    color: var(--ink);
    letter-spacing: 1px;
  }
  .subtitle {
    position: absolute;
    top: 865px;
    left: 38px;
    margin: 0;
    font-family: "Noto Serif JP", serif;
    font-weight: 700;
    font-size: 48px;
    line-height: 62px;
    color: var(--ink);
  }
</style>
</head>
<body>
  <main class="cover">
    <section class="title-panel">
      <h1 class="title-line first">現場を</h1>
      <h1 class="title-line second"><span class="highlight">変</span>える</h1>
      <div class="title-lead">人が<span class="gap"></span>大切にする</div>
      <div class="title-main">４つの視点</div>
      <div class="author">南谷 睦月</div>
    </section>
    <div class="growth-scene" role="img" aria-label="木のブロックを階段状に積み上げ、赤い上向き矢印を描いた成長を表す写真"></div>
    <p class="tagline">最初の一歩を踏み出せない、あなたへ。</p>
    <p class="subtitle">挑戦した人々の<br>物語から、<br>静かに学び取る。</p>
  </main>
</body>
</html>
```